Website Design for a Project Management Consulting Business

I have a logo design already and now I need a website.
I am a project manager and run my own consulting business.
Currently I am under contract with 3 major Kestrelmark 300 companies. I'd like a website I can direct current and future clients.
My job is running IT projects and working with developers to deliver business priorities.
The website should be professional and clean - I work IT projects and would like to incorporate that into any theme.
I'd like the site to have several page or breakoff links - sections would include : about me, about my services, a page to display all of my certification badges, another page to talk about highlights from past projects and so on.
Looking for a collaborative experience.

Industry/Entity Type

Kestrelmark 300 Consulting Firm - Project Management

Coding

Coded - Design and coding required

Number of Pages Required

1 page

Font styles to use
Serif

Colors
0094D4
00A9DD
6FCCEA
C7EBF8
E9F6FB
EE7325
F08F49
F5BC92
FAE3D3
FDF4ED

Requirements
Must have
• Sections that are a must: About Me (bio), About My Services, About my Certifications and Credentials, Experience on Past Projects,
Nice to have
• I have added the logo below - I'd like to use the logo and have it prominent ; should be professional and inviting

```html
<!DOCTYPE html>
<html lang="en">
<head>
<meta charset="utf-8">
<title>Meridian Project Management</title>
<link href="https://fonts.googleapis.com/css2?family=Michroma&family=Poppins:wght@400;500;600;700&display=swap" rel="stylesheet">
<style>
:root{
  --navy:#061d45;
  --navy-2:#0a2c63;
  --blue:#0a6fd8;
  --blue-bright:#0094d4;
  --sky:#00a9dd;
  --pale:#c7ebf8;
  --mist:#eef2f6;
  --ink:#14203a;
  --muted:#5a6478;
  --white:#ffffff;
}
*{box-sizing:border-box;margin:0;padding:0}
html,body{width:1200px;height:3868px;overflow:hidden}
body{font-family:"Poppins",sans-serif;color:var(--ink);background:var(--white);position:relative}
.display{font-family:"Michroma",sans-serif;text-transform:uppercase;letter-spacing:1px}
.btn{display:inline-block;font-family:"Poppins",sans-serif;font-weight:600;font-size:13px;letter-spacing:1px;text-transform:uppercase;color:var(--white);background:var(--blue);padding:14px 30px}
.btn-outline{background:transparent;border:1.5px solid var(--white);padding:10px 24px;font-size:11px}

/* header + hero */
.hero{position:absolute;left:0;top:0;width:1200px;height:760px;overflow:hidden}
.hero-photo{position:absolute;inset:0;background:linear-gradient(100deg,#04112c 0%,#0a2a5e 45%,#0e58b8 75%,#0b3b86 100%)}
.hero-glow{position:absolute;right:0;top:0;width:620px;height:760px;background:radial-gradient(circle at 65% 45%,rgba(0,148,212,.55),rgba(0,0,0,0) 60%)}
.site-nav{position:absolute;left:0;top:0;width:1200px;height:86px;display:flex;align-items:center;justify-content:space-between;padding:0 60px 0 40px;background:rgba(4,17,44,.75)}
.brand{display:flex;align-items:center;gap:12px;color:var(--white);font-weight:700;font-size:22px;letter-spacing:1px;text-transform:uppercase}
.brand-mark{width:34px;height:34px;background:var(--blue-bright)}
.menu{display:flex;gap:44px;list-style:none}
.menu li{font-size:13px;letter-spacing:1.5px;color:#c5d2e8;text-transform:uppercase}
.menu li.active{color:var(--white);font-weight:600;border-bottom:2px solid var(--white);padding-bottom:4px}
.hero-copy{position:absolute;left:100px;top:262px;color:var(--white)}
.hero-copy .kicker{font-size:17px;letter-spacing:3px;margin-bottom:18px}
.hero-copy h1{font-family:"Michroma",sans-serif;font-weight:400;font-size:46px;line-height:1.2;text-transform:uppercase;letter-spacing:1px}
.hero-copy .btn{margin-top:36px}

/* about */
.about{position:absolute;left:0;top:760px;width:1200px;height:520px}
.about-frame{position:absolute;left:120px;top:60px;width:410px;height:430px;border:6px solid var(--navy-2)}
.about-photo{position:absolute;left:140px;top:48px;width:386px;height:420px;background:linear-gradient(160deg,#c9ccd2,#7d828c 60%,#4b5260)}
.about-copy{position:absolute;left:586px;top:80px;width:500px}
.label{font-size:14px;letter-spacing:2.5px;color:var(--blue);text-transform:uppercase}
.about-copy h2{font-family:"Michroma",sans-serif;font-weight:400;font-size:40px;color:var(--navy-2);text-transform:uppercase;margin:4px 0 26px}
.about-copy p{font-size:15px;line-height:1.75;color:#2b3448;margin-bottom:22px}
.about-copy .btn{margin-top:4px}

/* services */
.services{position:absolute;left:0;top:1280px;width:1200px;height:690px}
.services svg.bg{position:absolute;inset:0}
.section-head{position:absolute;left:0;width:1200px;text-align:center;color:var(--white)}
.section-head .label{color:var(--pale);font-size:14px}
.section-head h2{font-family:"Michroma",sans-serif;font-weight:400;font-size:40px;text-transform:uppercase;margin-top:4px}
.section-head .rule{width:70px;height:2px;background:currentColor;margin:14px auto 0;opacity:.7}
.service-card{position:absolute;top:180px;width:306px;height:420px;background:var(--navy-2);border-radius:0 60px 0 0;padding:34px 30px;color:var(--white)}
.service-icon{width:76px;height:76px;border-radius:50%;border:2px solid var(--white);display:flex;align-items:center;justify-content:center;margin-left:60px;margin-bottom:40px}
.service-card h3{font-weight:700;font-size:19px;text-transform:uppercase;line-height:1.25}
.service-card h3 span{display:block;font-weight:400}
.service-card p{font-size:12.5px;line-height:1.65;color:#c6d3ea;margin:14px 0 28px}

/* certificates */
.certs{position:absolute;left:0;top:1970px;width:1200px;height:530px;background:linear-gradient(180deg,#f3f5f8,#e5e9ef)}
.certs .section-head{color:var(--navy-2);top:58px}
.certs .section-head .label{color:var(--blue)}
.cert-card{position:absolute;top:160px;width:320px;height:270px;background:var(--white);border-radius:12px;box-shadow:0 10px 24px rgba(10,40,90,.12);padding:28px 26px}
.badges{display:flex;gap:18px;justify-content:center;height:130px;align-items:center}
.badge{width:104px;height:104px;border-radius:50%}
.badge-diamond{width:86px;height:86px;transform:rotate(45deg);border-radius:8px}
.cert-card .org{font-size:13px;color:var(--blue);margin-top:28px}
.cert-card .org-name{font-size:17px;font-weight:500;color:var(--ink)}
.cert-rule{position:absolute;left:0;right:0;bottom:0;height:5px;background:var(--blue);border-radius:0 0 12px 12px}

/* projects */
.projects{position:absolute;left:0;top:2500px;width:1200px;height:480px}
.projects-copy{position:absolute;left:100px;top:130px;width:290px}
.projects-copy h2{font-family:"Michroma",sans-serif;font-weight:400;font-size:38px;line-height:1.25;color:var(--navy-2);text-transform:uppercase;margin-top:6px}
.projects-copy .rule{width:80px;height:2px;background:var(--blue);margin:16px 0}
.projects-copy p{font-size:13px;line-height:1.6;color:var(--muted)}
.arrows{display:flex;gap:22px;margin-top:28px}
.project{position:absolute;top:105px;height:300px;overflow:hidden}
.project-photo{position:absolute;inset:0}
.project-caption{position:absolute;left:0;right:0;bottom:0;padding:18px 26px;background:linear-gradient(180deg,rgba(6,29,69,0),rgba(6,29,69,.9));color:var(--white)}
.project-caption small{font-size:13px;display:block;color:#cfe0f5}
.project-caption strong{font-size:18px;font-weight:600;line-height:1.3;display:block}

/* contact */
.contact{position:absolute;left:0;top:2980px;width:1200px;height:600px}
.contact svg.bg{position:absolute;inset:0}
.contact-photo-frame{position:absolute;left:140px;top:170px;width:410px;height:340px;border:5px solid var(--white)}
.contact-photo{position:absolute;left:160px;top:150px;width:400px;height:340px;background:linear-gradient(135deg,#1d4f9e,#5d85c7 50%,#0b2a5e)}
.contact-form{position:absolute;left:636px;top:90px;width:400px;color:var(--white)}
.contact-form .label{color:var(--pale)}
.contact-form h2{font-family:"Michroma",sans-serif;font-weight:400;font-size:40px;text-transform:uppercase;margin:4px 0 30px}
.field{border-bottom:1px solid rgba(255,255,255,.55);font-size:13px;padding:0 0 12px;margin-bottom:30px;color:#dbe6f6}
.field.tall{height:80px}
.contact-form .btn{margin-top:4px}

/* footer */
.site-footer{position:absolute;left:0;top:3580px;width:1200px;height:288px;border-top:4px solid var(--blue)}
.footer-brand{position:absolute;left:120px;top:50px}
.footer-brand .brand{color:var(--navy-2);font-size:20px}
.socials{display:flex;gap:10px;margin-top:28px}
.socials span{width:30px;height:30px;border-radius:50%;background:var(--navy-2)}
.copyright{font-size:12px;color:var(--muted);margin-top:18px}
.footer-col{position:absolute;top:56px}
.footer-col h4{font-size:14px;font-weight:600;letter-spacing:1.5px;text-transform:uppercase;color:var(--navy-2);padding-bottom:10px;border-bottom:2px solid var(--blue);display:inline-block;margin-bottom:16px}
.footer-col li{list-style:none;font-size:13px;color:#3a4458;margin-bottom:11px}
.contact-line{display:flex;align-items:center;gap:12px;font-size:13px;color:#3a4458;margin-bottom:14px;line-height:1.35}
.contact-line .ico{width:32px;height:32px;border-radius:50%;background:var(--blue);display:flex;align-items:center;justify-content:center;flex:none}
</style>
</head>
<body>

<header class="hero">
  <div class="hero-photo" role="img" aria-label="Night city skyline with the consultant standing in a suit beside a rising blue arrow"></div>
  <div class="hero-glow"></div>
  <nav class="site-nav">
    <div class="brand"><span class="brand-mark"></span>Meridian Project Management</div>
    <ul class="menu">
      <li class="active">About me</li>
      <li>Services</li>
      <li>Projects</li>
      <li>Certificates</li>
      <li>Contact</li>
    </ul>
  </nav>
  <div class="hero-copy">
    <p class="kicker">WELCOME TO MERIDIAN</p>
    <h1>Project<br>Management<br>Consulting</h1>
    <a class="btn">Learn more</a>
  </div>
</header>

<section class="about">
  <div class="about-frame"></div>
  <div class="about-photo" role="img" aria-label="Portrait of the consultant in a grey suit"></div>
  <div class="about-copy">
    <p class="label">My bio</p>
    <h2>About me</h2>
    <p>Lorem ipsum dolor sit amet, consectetur adipiscing elit, sed do eiusmod tempor incididunt ut labore et dolore magna aliqua. Ut enim ad minim veniam, quis nostrud exercitation ullamco laboris nisi ut aliquip ex ea commodo consequat.</p>
    <p>Duis aute irure dolor in reprehenderit in voluptate velit esse cillum dolore eu fugiat nulla pariatur. Excepteur sint occaecat cupidatat non proident, sunt in culpa qui officia deserunt mollit anim id est laborum.</p>
    <a class="btn">Learn more</a>
  </div>
</section>

<section class="services">
  <svg class="bg" width="1200" height="690" viewBox="0 0 1200 690" aria-hidden="true">
    <defs>
      <linearGradient id="svcGrad" x1="0" y1="0" x2="1" y2="1">
        <stop offset="0" stop-color="#0a7be0"/>
        <stop offset="1" stop-color="#0559c2"/>
      </linearGradient>
    </defs>
    <path d="M0 20 Q300 -10 560 40 Q800 90 1000 30 Q1110 0 1200 10 L1200 690 L0 690 Z" fill="url(#svcGrad)"/>
    <path d="M820 0 Q1000 60 1200 0 L1200 120 Q1040 40 820 0 Z" fill="#0a2c63" opacity=".5"/>
  </svg>
  <div class="section-head" style="top:60px">
    <p class="label">What we do</p>
    <h2>My services</h2>
    <div class="rule"></div>
  </div>

  <article class="service-card" style="left:100px">
    <div class="service-icon">
      <svg width="40" height="40" viewBox="0 0 40 40" fill="none" stroke="#fff" stroke-width="2"><circle cx="20" cy="14" r="6"/><path d="M8 34c0-7 5-11 12-11s12 4 12 11"/></svg>
    </div>
    <h3>Consulting<span>services</span></h3>
    <p>Lorem ipsum dolor sit amet, conse ctetur adipiscing elit, sed do eiusmod tempor incididunt ut labore et dolore magna aliqua. Ut enim ad minim.</p>
    <a class="btn btn-outline">Learn more</a>
  </article>
  <article class="service-card" style="left:447px">
    <div class="service-icon">
      <svg width="40" height="40" viewBox="0 0 40 40" fill="none" stroke="#fff" stroke-width="2"><rect x="6" y="8" width="28" height="20"/><path d="M12 22l6-6 4 4 6-7"/><path d="M14 34h12M20 28v6"/></svg>
    </div>
    <h3>Project<span>management</span></h3>
    <p>Lorem ipsum dolor sit amet, conse ctetur adipiscing elit, sed do eiusmod tempor incididunt ut labore et dolore magna aliqua. Ut enim ad minim.</p>
    <a class="btn btn-outline">Learn more</a>
  </article>
  <article class="service-card" style="left:794px">
    <div class="service-icon">
      <svg width="40" height="40" viewBox="0 0 40 40" fill="none" stroke="#fff" stroke-width="2"><circle cx="16" cy="18" r="6"/><path d="M16 8v4M16 24v4M6 18h4M22 18h4M9 11l3 3M20 22l3 3M9 25l3-3M20 14l3-3"/><circle cx="29" cy="29" r="4"/></svg>
    </div>
    <h3>Consultancy<span>and training</span></h3>
    <p>Lorem ipsum dolor sit amet, conse ctetur adipiscing elit, sed do eiusmod tempor incididunt ut labore et dolore magna aliqua. Ut enim ad minim.</p>
    <a class="btn btn-outline">Learn more</a>
  </article>
</section>

<section class="certs">
  <div class="section-head">
    <p class="label">My certificates</p>
    <h2>Certificates</h2>
    <div class="rule" style="background:var(--blue)"></div>
  </div>

  <article class="cert-card" style="left:100px">
    <div class="badges">
      <span class="badge" style="background:#2b2466"></span>
      <span class="badge" style="background:#3a2e7a"></span>
    </div>
    <p class="org">Organization</p>
    <p class="org-name">Institute of Delivery Leaders</p>
    <div class="cert-rule"></div>
  </article>
  <article class="cert-card" style="left:440px">
    <div class="badges">
      <span class="badge" style="background:#f0a43a"></span>
      <span class="badge" style="background:#ee7325"></span>
    </div>
    <p class="org">Organization</p>
    <p class="org-name">AgileGuild</p>
    <div class="cert-rule"></div>
  </article>
  <article class="cert-card" style="left:780px">
    <div class="badges" style="gap:44px">
      <span class="badge-diamond" style="background:#1f3f6e"></span>
      <span class="badge-diamond" style="background:#2f5a8f"></span>
    </div>
    <p class="org">Organization</p>
    <p class="org-name">Tiered Agile Council</p>
    <div class="cert-rule"></div>
  </article>
</section>

<section class="projects">
  <div class="projects-copy">
    <p class="label">Projects</p>
    <h2>Latest<br>projects</h2>
    <div class="rule"></div>
    <p>Lorem ipsum dolor sit amet, conse ctetur adipiscing elit, sed do eiusmod.</p>
    <div class="arrows">
      <svg width="18" height="28" viewBox="0 0 18 28"><path d="M14 3L4 14l10 11" fill="none" stroke="#0a2c63" stroke-width="3"/></svg>
      <svg width="18" height="28" viewBox="0 0 18 28"><path d="M4 3l10 11L4 25" fill="none" stroke="#0a6fd8" stroke-width="3"/></svg>
    </div>
  </div>
  <article class="project" style="left:400px;width:400px">
    <div class="project-photo" role="img" aria-label="Operations room with engineers working at rows of monitors" style="background:linear-gradient(140deg,#0b2352,#1c4f9a 55%,#0a1a3c)"></div>
    <div class="project-caption">
      <small>Simple dummy text</small>
      <strong>Lorem Ipsum is simply dummy text of the printing and typesetting</strong>
    </div>
  </article>
  <article class="project" style="left:820px;width:380px">
    <div class="project-photo" role="img" aria-label="Team meeting around a table with laptops in a bright office" style="background:linear-gradient(140deg,#8a7a6a,#c9b8a4 50%,#5a6070)"></div>
    <div class="project-caption">
      <small>Simple dummy text</small>
      <strong>Lorem Ipsum is simply dummy text of the printing and typesetting</strong>
    </div>
  </article>
</section>

<section class="contact">
  <svg class="bg" width="1200" height="600" viewBox="0 0 1200 600" aria-hidden="true">
    <path d="M0 60 Q0 0 80 10 Q500 70 900 20 Q1080 0 1200 30 L1200 600 L0 600 Z" fill="#0a2c63"/>
    <path d="M0 600 L0 300 Q300 520 1200 420 L1200 600 Z" fill="#061d45"/>
  </svg>
  <div class="contact-photo-frame"></div>
  <div class="contact-photo" role="img" aria-label="Businessman in a suit reaching toward a bright upward arrow"></div>
  <div class="contact-form">
    <p class="label">Get in touch</p>
    <h2>Contact me</h2>
    <div class="field">Name</div>
    <div class="field">Phone Number</div>
    <div class="field">Email address</div>
    <div class="field tall">Message</div>
    <a class="btn">Send enquiry</a>
  </div>
</section>

<footer class="site-footer">
  <div class="footer-brand">
    <div class="brand"><span class="brand-mark"></span>Meridian</div>
    <div class="socials"><span></span><span></span><span></span><span></span></div>
    <p class="copyright">Copyright 2022 Meridian LLC All Rights Reserved</p>
  </div>
  <div class="footer-col" style="left:490px">
    <h4>Navigation</h4>
    <ul><li>About Me</li><li>Services Provide</li><li>Projects</li><li>Certifications</li></ul>
  </div>
  <div class="footer-col" style="left:680px">
    <h4>Resources</h4>
    <ul><li>Support</li><li>Privacy Policy</li><li>Contact Us</li></ul>
  </div>
  <div class="footer-col" style="left:880px">
    <h4>Contact us</h4>
    <div class="contact-line">
      <span class="ico"><svg width="14" height="16" viewBox="0 0 14 16"><path d="M7 1a5 5 0 0 0-5 5c0 4 5 9 5 9s5-5 5-9a5 5 0 0 0-5-5z" fill="#fff"/><circle cx="7" cy="6" r="2" fill="#0a6fd8"/></svg></span>
      <span>5420 Harbor Ridge Road<br>12 Linden Avenue, Ashford</span>
    </div>
    <div class="contact-line">
      <span class="ico"><svg width="14" height="14" viewBox="0 0 14 14"><path d="M3 1l2 3-1.5 1.5a8 8 0 0 0 5 5L10 9l3 2-1 2c-6 0-11-5-11-11z" fill="#fff"/></svg></span>
      <span>(555) 014-7721</span>
    </div>
    <div class="contact-line">
      <span class="ico"><svg width="16" height="12" viewBox="0 0 16 12"><rect x="1" y="1" width="14" height="10" fill="none" stroke="#fff" stroke-width="1.5"/><path d="M1 1l7 6 7-6" fill="none" stroke="#fff" stroke-width="1.5"/></svg></span>
      <span>hello@meridianpm.example</span>
    </div>
  </div>
</footer>

</body>
</html>
```